Dental marketing ad poster

I recently opened a new dental practice about 2 months ago and would like to have an ad designed for an A-frame poster to place outside our office. The goal of this ad is to attract and appeal to potential patients so they feel encouraged to come into the practice.
I’m leaving the creative direction up to you—I’d like to see what you can come up with. The ad can be funny or serious, but it should be eye-catching and patient-focused. Please highlight that we provide crowns, implants and teeth whitening.
My theme color is green but I’ll accept any color
Let me see your ideas!
Dentistry

```html
<!DOCTYPE html>
<html lang="en">
<head>
<meta charset="utf-8">
<title>Maplewood Dentistry – A-frame poster</title>
<link rel="stylesheet" href="https://fonts.googleapis.com/css2?family=Nunito:wght@800;900&family=Outfit:wght@500&display=swap">
<style>
  :root {
    --page-bg: #e4e4e4;
    --paper: #ffffff;
    --brand-blue: #0b4f9e;
    --panel-blue: #0a60b2;
    --panel-blue-light: #2a86d0;
    --accent-blue: #7cc4f0;
    --leaf-green: #8cc63f;
    --photo-light: #eef0f2;
    --photo-mid: #c9ced6;
    --photo-shadow: #6e86a8;
  }
  * { margin: 0; padding: 0; box-sizing: border-box; }
  html, body { width: 1091px; height: 1200px; overflow: hidden; background: var(--page-bg); }
  .poster {
    position: absolute; left: 117px; top: 40px;
    width: 857px; height: 1120px;
    background: var(--paper);
    overflow: hidden;
  }
  .poster__art { position: absolute; inset: 0; width: 100%; height: 100%; }
  .brand {
    position: absolute; top: 72px; left: 0; width: 100%;
    text-align: center;
    font-family: "Nunito", sans-serif; font-weight: 800;
    font-size: 56px; letter-spacing: -0.5px;
    color: var(--brand-blue);
  }
  .headline { margin: 0; }
  .headline__line {
    position: absolute; left: 0; width: 100%; text-align: center;
    font-family: "Nunito", sans-serif; font-weight: 900;
    line-height: 1; letter-spacing: -1px;
  }
  .headline__line--top { top: 566px; font-size: 100px; color: var(--paper); }
  .headline__line--mid { top: 686px; font-size: 60px; color: var(--paper); }
  .headline__line--key { top: 752px; font-size: 180px; letter-spacing: -3px; color: var(--accent-blue); }
  .services {
    position: absolute; top: 972px; left: 0; width: 100%;
    text-align: center;
    font-family: "Outfit", sans-serif; font-weight: 500;
    font-size: 34px; line-height: 1.3;
    color: var(--paper);
  }
</style>
</head>
<body>
  <main class="poster">
    <svg class="poster__art" viewBox="0 0 857 1120" preserveAspectRatio="none">
      <defs>
        <linearGradient id="photoTone" x1="0" y1="0" x2="1" y2="1">
          <stop offset="0" stop-color="var(--photo-light)"/>
          <stop offset=".55" stop-color="var(--photo-mid)"/>
          <stop offset="1" stop-color="var(--photo-shadow)"/>
        </linearGradient>
        <radialGradient id="panelTone" cx=".5" cy=".75" r=".7">
          <stop offset="0" stop-color="var(--panel-blue-light)"/>
          <stop offset="1" stop-color="var(--panel-blue)"/>
        </radialGradient>
      </defs>
      <rect class="photo-area" x="0" y="160" width="857" height="560" fill="url(#photoTone)"
            role="img" aria-label="Photo of a dentist examining a patient in a dental chair"/>
      <path class="band-green" fill="var(--leaf-green)"
            d="M0 300 C200 215 560 250 857 180 V160 C560 230 200 195 0 275 Z"/>
      <path class="band-white" fill="var(--paper)"
            d="M0 0 H857 V165 C560 235 200 200 0 278 Z"/>
      <path class="panel-blue" fill="url(#panelTone)"
            d="M0 560 C300 620 560 600 857 540 V1120 H0 Z"/>
    </svg>

    <div class="brand">Maplewood Dentistry</div>

    <h1 class="headline">
      <span class="headline__line headline__line--top">Take care</span>
      <span class="headline__line headline__line--mid">of your</span>
      <span class="headline__line headline__line--key">teeth</span>
    </h1>

    <p class="services">WE PROVIDE CROWNS, IMPLANTS<br>AND TEETH WHITENING.</p>
  </main>
</body>
</html>
```